Wordpress website design for a high-end painting business

We are currently rebranding and are looking to update our Wordpress theme. We have recently rebranded our logo on ArtHatchery, and would like our website to be equally as refined.
Our business is named “Holloway Coatings”. We are a high-end painting business that is known for being professional and having high standards. Our clean and professional image is important as it separates us from our competition. Our current website can be found at www.hollowayfinishes.co.nz . We designed the site ourselves so it is understandably rudimentary. We are generally happy with the. page layout of our existing site, but we like a professional remodel. Any ideas on improvement welcomed.
We would like the front page of the website to summarise all of the info throughout the whole website (I.e introduction, photos, testimonials, contact info etc.) as visitors typically scroll through the first page to see that we are reputable and get to our contact number/email contact at the bottom of the page. We would like this first page to give a clean well rounded image of our business. We would like the gallery to be a scroll through of large photos, as it is difficult to see paint details in smaller photos. A contact page with an enquiry section would also be good.
For the colour scheme, we would like something that fits a bold, masculine and high end theme (similar to our logo attached).
We would like the footer to include Velnor paint logos and the accredited painter logo we have included as these are important to our profession.
We have attached some photos of our work also. I will add more in the coming days. More can also be found on our website.
If you have questions or comments, please don’t hesitate to ask and I will get back as soon as possible.
We are open to your own interpretation or ideas for a better layout/site provided they fit the general brief of being a well rounded site for our profession.
Thanks,
Holloway Coatings.
Target Market(s)
High end clients
Industry/Entity Type
Painting (interior and exterior)
Coding
Coded - Design and coding required
Requirements
Must have
- Classy feel, separating us from typical painting companies. Well rounded homepage.
Nice to have
- Lots of examples of our work
Should not have
- Untidy paint motifs (eg, paint droplets, paint splashes)

```html
<!DOCTYPE html>
<html lang="en">
<head>
<meta charset="utf-8">
<title>Holloway Coatings</title>
<link href="https://fonts.googleapis.com/css2?family=Merriweather:wght@700;900&family=Roboto:wght@400;500;700&display=swap" rel="stylesheet">
<style>
:root{
  --brown:#7a5a37;
  --brown-dark:#5e4428;
  --ink:#1b1e29;
  --footer:#131722;
  --paper:#f2f3f5;
  --text:#6b6f78;
  --white:#ffffff;
}
*{box-sizing:border-box;margin:0;padding:0}
html,body{width:1200px;height:3713px;overflow:hidden}
body{position:relative;font-family:'Roboto',sans-serif;color:var(--ink);background:var(--white)}
.abs{position:absolute}
.btn{position:absolute;display:flex;align-items:center;justify-content:center;border-radius:30px;font-weight:700;font-size:14px;text-transform:uppercase}

/* header */
.topbar{left:545px;top:0;width:538px;height:45px;background:var(--ink);border-radius:0 0 40px 40px;display:flex;align-items:center;padding-left:60px;gap:30px;color:#fff;font-size:14px;z-index:2}
.topbar span{display:flex;align-items:center;gap:14px}
.topbar i{width:32px;height:32px;border-radius:50%;background:#fff;display:flex;align-items:center;justify-content:center}
.header{left:0;top:0;width:1200px;height:102px;background:#fff}
.nav{right:117px;top:66px;display:flex;gap:45px;font-family:'Merriweather',serif;font-size:14px;font-weight:700}
.nav a{color:var(--ink);text-decoration:none}
.nav a.active{color:var(--brown)}
.brand{left:70px;top:-30px;width:178px;height:200px;border-radius:50%;background:#fff;display:flex;flex-direction:column;align-items:center;justify-content:flex-end;padding-bottom:36px;z-index:3}
.brand b{font-family:'Merriweather',serif;font-size:17px;color:var(--ink);text-align:center;line-height:1.2}

/* hero */
.hero{left:0;top:102px;width:1200px;height:601px;border-bottom-right-radius:300px 300px;background:linear-gradient(180deg,#5d7890 0%,#a89a7c 30%,#8d8066 55%,#3f5a2c 82%,#5a7a38 100%);overflow:hidden}
.hero::after{content:"";position:absolute;inset:0;background:rgba(20,20,25,.25)}
.hero-copy{left:0;top:310px;width:1200px;text-align:center;color:#fff;z-index:2}
.hero-copy h1{font-family:'Merriweather',serif;font-size:31px;font-weight:900;letter-spacing:.5px}
.hero-copy p{font-size:18px;font-weight:500;line-height:27px;margin-top:14px}
.hero .arrow,.slide-arrow{position:absolute;width:37px;height:37px;border-radius:50%;display:flex;align-items:center;justify-content:center}
.hero .arrow{background:#fff;top:282px;z-index:2}
.scroll{left:564px;top:667px;width:72px;height:72px;border-radius:50%;background:#fff;border:3px solid #e1e2e5;display:flex;align-items:center;justify-content:center;z-index:3}
.scroll span{width:46px;height:46px;border-radius:50%;background:var(--ink);display:flex;align-items:center;justify-content:center}

/* about */
.about{left:0;top:703px;width:1200px;height:524px;background:var(--paper)}
.about-art{left:118px;top:80px;width:354px;height:354px;border-radius:50%;background:radial-gradient(circle at 50% 50%,#2a2e3a 0%,var(--ink) 55%,#3b3326 80%,var(--brown) 100%);box-shadow:0 0 0 6px var(--paper),0 0 0 8px rgba(122,90,55,.35)}
.h2{font-family:'Merriweather',serif;font-weight:900;font-size:30px;text-transform:uppercase;line-height:38px}
.h2 em{font-style:normal;color:var(--brown)}
.about-copy{left:644px;top:87px;width:445px}
.about-copy p{font-size:13px;line-height:24px;color:var(--text);margin-top:14px}
.about-copy p:first-of-type{margin-top:26px}

/* services */
.title{left:0;width:1200px;text-align:center;font-size:36px}
.svc{position:absolute;top:1390px;width:231px;text-align:center}
.svc .pic{width:231px;height:231px;border-radius:50%;border-bottom:4px solid var(--ink)}
.svc .ico{position:absolute;left:70px;top:180px;width:92px;height:92px;border-radius:50%;background:var(--ink);display:flex;align-items:center;justify-content:center}
.svc h3{margin-top:72px;font-size:20px;font-weight:700;color:var(--brown);line-height:26px;text-transform:uppercase}
.slide-arrow{border:2px solid var(--ink);top:1502px;background:#fff}

/* testimonials */
.reviews{left:0;top:1800px;width:1200px;height:496px;background:linear-gradient(180deg,#6a5238 0%,#7c6040 50%,#6a4f33 100%)}
.reviews h2{position:absolute;top:52px;width:1200px;text-align:center;color:#fff;font-family:'Merriweather',serif;font-size:27px;font-weight:900}
.card{position:absolute;top:125px;width:309px;height:273px;background:#fff;border-radius:8px;text-align:center;padding:18px 18px 0}
.avatar{width:75px;height:75px;border-radius:50%;margin:0 auto 16px}
.card p{font-size:13px;line-height:25px;color:var(--text);position:relative;z-index:1}
.card .q{position:absolute;font-family:'Merriweather',serif;font-size:80px;color:#e6e6e8;line-height:1}
.card h4{position:absolute;bottom:14px;left:0;width:100%;font-family:'Merriweather',serif;font-size:13px;color:var(--brown)}
.dots{top:2230px;left:572px;display:flex;gap:5px}
.dots i{width:9px;height:9px;border-radius:50%;background:#c9c0b6}
.dots i.on{background:#fff}

/* projects */
.projects{left:0;top:2296px;width:1200px;height:516px;overflow:hidden}
.proj{position:absolute;top:163px;width:231px;height:255px;background:#fff;border-radius:6px;box-shadow:0 2px 10px rgba(0,0,0,.1);padding:5px}
.proj .ph{height:178px;border-radius:3px}
.proj .meta{text-align:center;font-size:13px;line-height:26px;margin-top:14px;color:var(--ink);text-transform:uppercase}
.proj .meta svg{vertical-align:-2px;margin-right:8px}

/* contact */
.contact{left:0;top:2812px;width:1200px;height:501px;background:var(--paper)}
.info{position:absolute;left:111px;display:flex;gap:27px}
.info .c{width:81px;height:81px;border-radius:50%;background:#fff;box-shadow:0 3px 10px rgba(0,0,0,.08);display:flex;align-items:center;justify-content:center;flex:none}
.info h5{font-family:'Merriweather',serif;font-size:14px;text-transform:uppercase;margin-top:8px}
.info p{font-size:14px;color:var(--text);line-height:21px;margin-top:6px}
.field{position:absolute;background:#fff;border:1px solid #e3e4e7;border-radius:2px;font-size:14px;color:var(--text);display:flex;align-items:center;gap:8px;padding-left:16px}
.field.msg{align-items:flex-start;padding-top:14px}

/* footer */
.footer{left:0;top:3313px;width:1200px;height:400px;background:var(--footer);border-top-left-radius:150px;color:#fff}
.flogo{left:111px;top:58px;width:150px;height:150px;border-radius:50%;border:2px solid #fff;display:flex;align-items:center;justify-content:center;text-align:center;font-family:'Merriweather',serif;font-size:17px;font-weight:700;line-height:1.25}
.fcol{position:absolute;top:58px}
.fcol h6{font-family:'Merriweather',serif;font-size:16px;font-weight:700;text-transform:uppercase;margin-bottom:16px}
.fcol li{list-style:none;font-size:14px;line-height:25px;display:flex;gap:14px;align-items:flex-start}
.fcol li i{width:11px;height:11px;border-radius:50%;border:2px solid var(--brown);margin-top:7px;flex:none}
.rule{left:111px;width:977px;height:1px;background:#3a3f4c}
.badge{left:339px;top:285px;display:flex;align-items:center;gap:8px}
.badge .panel{height:46px;background:#fff;border-radius:2px;border:3px solid #fff;box-shadow:inset 0 0 0 2px var(--ink)}
.badge .tab{width:14px;height:52px;background:#fff;border-radius:2px}
.copy{left:0;top:3676px;width:1200px;text-align:center;font-size:12px;color:#d5d7dc;font-family:'Merriweather',serif}
</style>
</head>
<body>

<div class="abs header"></div>
<div class="abs topbar">
  <span><i><svg width="14" height="14" viewBox="0 0 24 24"><path fill="#1b1e29" d="M6.6 10.8a15 15 0 006.6 6.6l2.2-2.2a1 1 0 011-.25 11 11 0 003.6.6 1 1 0 011 1V20a1 1 0 01-1 1A17 17 0 013 4a1 1 0 011-1h3.5a1 1 0 011 1c0 1.3.2 2.5.6 3.6a1 1 0 01-.25 1z"/></svg></i>021 555 0148</span>
  <span><i><svg width="14" height="14" viewBox="0 0 24 24"><path fill="#1b1e29" d="M2 5h20v14H2z"/><path d="M3 6l9 7 9-7" stroke="#fff" stroke-width="2" fill="none"/></svg></i>studio@hollowaycoatings.co.nz</span>
</div>
<div class="abs brand"><b>HOLLOWAY<br>COATINGS</b></div>
<nav class="abs nav">
  <a class="active" href="#">HOME</a><a href="#">ABOUT</a><a href="#">SERVICES</a><a href="#">TESTIMONIALS</a><a href="#">PROJECT</a><a href="#">CONTACT</a>
</nav>

<section class="abs hero" role="img" aria-label="Photograph of a freshly painted two storey home with a garden">
  <span class="arrow" style="left:41px"><svg width="12" height="12" viewBox="0 0 12 12"><path d="M8 1L3 6l5 5" stroke="#1b1e29" stroke-width="2" fill="none"/></svg></span>
  <span class="arrow" style="left:1122px"><svg width="12" height="12" viewBox="0 0 12 12"><path d="M4 1l5 5-5 5" stroke="#1b1e29" stroke-width="2" fill="none"/></svg></span>
</section>
<div class="abs hero-copy">
  <h1>WELCOME TO HOLLOWAY COATINGS</h1>
  <p>Holloway Coatings Here at Holloway Coatings, we take a<br>lot of pride in our work.</p>
</div>
<div class="btn" style="left:526px;top:435px;width:147px;height:49px;background:#fff;color:var(--brown);z-index:3">Get Started</div>
<div class="abs scroll"><span><svg width="16" height="16" viewBox="0 0 16 16"><path d="M3 6l5 5 5-5" stroke="#fff" stroke-width="2" fill="none"/></svg></span></div>

<section class="abs about">
  <div class="abs about-art" role="img" aria-label="Large brand emblem illustration in navy and bronze"></div>
  <div class="abs about-copy">
    <h2 class="h2">We take pride in<br><em>our work</em></h2>
    <p>Here at Holloway Coatings, we take a lot of pride in our work. We strive to ensure the highest quality paint-work, paying close attention to detail to provide a long lasting finish. Our clients are always our priority, we aim to deliver beyond their expectations.</p>
    <p>It is our goal to provide an excellent service from start to finish through clear communication, free quoting and transparency with our pricing.</p>
  </div>
  <div class="btn" style="left:644px;top:370px;width:137px;height:51px;background:var(--brown);color:#fff">Learn More</div>
</section>

<h2 class="abs title h2" style="top:1303px"><em>Our</em> Services</h2>
<span class="slide-arrow" style="left:41px"><svg width="12" height="12" viewBox="0 0 12 12"><path d="M8 1L3 6l5 5" stroke="#1b1e29" stroke-width="2" fill="none"/></svg></span>
<span class="slide-arrow" style="left:1122px"><svg width="12" height="12" viewBox="0 0 12 12"><path d="M4 1l5 5-5 5" stroke="#1b1e29" stroke-width="2" fill="none"/></svg></span>

<div class="svc" style="left:112px">
  <div class="pic" role="img" aria-label="Photo of a painted house exterior" style="background:linear-gradient(180deg,#8fb0d6 0%,#b9c4cc 40%,#6f6a62 60%,#4f7a35 100%)"></div>
  <div class="ico"><svg width="44" height="40" viewBox="0 0 44 40" fill="none" stroke="#fff" stroke-width="2"><path d="M3 18L22 4l19 14M8 15v22h28V15M14 24h6v13h-6zM25 24h7v6h-7z"/></svg></div>
  <h3>Exterior Painting</h3>
</div>
<div class="svc" style="left:360px">
  <div class="pic" role="img" aria-label="Photo of a painted kitchen interior" style="background:linear-gradient(160deg,#f1f1ef 0%,#d8d6d2 45%,#8b8a86 75%,#3e3e40 100%)"></div>
  <div class="ico"><svg width="40" height="44" viewBox="0 0 40 44" fill="none" stroke="#fff" stroke-width="2"><rect x="6" y="3" width="28" height="10" rx="2"/><path d="M34 8h3v10H20v6M17 24h6v17h-6z"/></svg></div>
  <h3>Interior Painting</h3>
</div>
<div class="svc" style="left:608px">
  <div class="pic" role="img" aria-label="Photo of a patterned green wallpaper feature wall" style="background:linear-gradient(120deg,#c7ccd0 0%,#6f8378 35%,#52665b 70%,#3c4b43 100%)"></div>
  <div class="ico"><svg width="40" height="44" viewBox="0 0 40 44" fill="none" stroke="#fff" stroke-width="2"><rect x="6" y="4" width="28" height="36"/><path d="M20 4v36M10 12l6 6M24 22l6 6M10 28l6 6"/></svg></div>
  <h3>Wallpapering</h3>
</div>
<div class="svc" style="left:857px">
  <div class="pic" role="img" aria-label="Photo of a cleaned brick and weatherboard home" style="background:linear-gradient(180deg,#5c8fd0 0%,#9ab6d6 40%,#7a5a4a 62%,#4e6d38 100%)"></div>
  <div class="ico"><svg width="44" height="44" viewBox="0 0 44 44" fill="none" stroke="#fff" stroke-width="2"><path d="M4 20L22 6l18 14M9 17v20h16M18 37V27h7M30 26l4 6M36 24v6M28 33h10v6H28z"/></svg></div>
  <h3>Waterblasting &amp;<br>House Cleaning</h3>
</div>

<section class="abs reviews" role="img" aria-label="Background photo of houses with a warm brown tint">
  <h2>WHAT OUR CLIENTS HAVE TO SAY</h2>
  <div class="card" style="left:111px">
    <div class="avatar" role="img" aria-label="Client portrait" style="background:linear-gradient(160deg,#e7b9a4,#9a5b48)"></div>
    <span class="q" style="left:18px;top:100px">&ldquo;</span><span class="q" style="right:18px;top:160px">&rdquo;</span>
    <p>Very happy with Holloway Coatings. Owen and Rowan did a great job with good communication and attention to detail. Definitely recommend... good value for money!</p>
    <h4>-PETER LINDQVIST</h4>
  </div>
  <div class="card" style="left:445px">
    <div class="avatar" role="img" aria-label="Client portrait" style="background:linear-gradient(160deg,#d0b8a2,#5e4b3e)"></div>
    <span class="q" style="left:18px;top:100px">&ldquo;</span><span class="q" style="right:18px;top:160px">&rdquo;</span>
    <p>Owen and Rowan was prompt and efficient. Very friendly and knowledgeable. Everything was done better than I expected. I would highly recommend them for anyone looking for painters.</p>
    <h4>-MARCUS HALE</h4>
  </div>
  <div class="card" style="left:779px">
    <div class="avatar" role="img" aria-label="Client portrait" style="background:linear-gradient(160deg,#a8b6c6,#4d5f78)"></div>
    <span class="q" style="left:18px;top:100px">&ldquo;</span><span class="q" style="right:18px;top:160px">&rdquo;</span>
    <p>We could not be happier with the work done painting the exterior of our two storey home. Owen and Rowan had brilliant communication and the job went very smoothly. Would definitely recommend!</p>
    <h4>-JULIA BRENNAN</h4>
  </div>
</section>
<div class="abs dots"><i></i><i class="on"></i><i></i><i></i></div>

<section class="abs projects">
  <h2 class="abs title h2" style="top:90px"><em>Recent</em> Projects</h2>
  <div class="proj" style="left:111px"><div class="ph" role="img" aria-label="Project photo: grey weatherboard house" style="background:linear-gradient(180deg,#c9d3dc 0%,#8e98a0 55%,#5f8242 100%)"></div><div class="meta"><svg width="13" height="13" viewBox="0 0 14 14"><path fill="#7a5a37" d="M1 3h12v10H1z"/></svg>02 MAR 2022<br><svg width="11" height="13" viewBox="0 0 12 14"><path fill="#7a5a37" d="M6 0a5 5 0 015 5c0 4-5 9-5 9S1 9 1 5a5 5 0 015-5z"/></svg>Waikato</div></div>
  <div class="proj" style="left:354px"><div class="ph" role="img" aria-label="Project photo: bright painted living room" style="background:linear-gradient(180deg,#eef0f2 0%,#c8ccd0 55%,#5d6570 100%)"></div><div class="meta"><svg width="13" height="13" viewBox="0 0 14 14"><path fill="#7a5a37" d="M1 3h12v10H1z"/></svg>02 MAR 2022<br><svg width="11" height="13" viewBox="0 0 12 14"><path fill="#7a5a37" d="M6 0a5 5 0 015 5c0 4-5 9-5 9S1 9 1 5a5 5 0 015-5z"/></svg>Hamilton</div></div>
  <div class="proj" style="left:598px"><div class="ph" role="img" aria-label="Project photo: navy clad house with deck" style="background:linear-gradient(180deg,#2f6fd0 0%,#5d6f94 50%,#9b5b34 100%)"></div><div class="meta"><svg width="13" height="13" viewBox="0 0 14 14"><path fill="#7a5a37" d="M1 3h12v10H1z"/></svg>02 MAR 2022<br><svg width="11" height="13" viewBox="0 0 12 14"><path fill="#7a5a37" d="M6 0a5 5 0 015 5c0 4-5 9-5 9S1 9 1 5a5 5 0 015-5z"/></svg>Hamilton</div></div>
  <div class="proj" style="left:840px"><div class="ph" role="img" aria-label="Project photo: painted dining room" style="background:linear-gradient(180deg,#e6e6e4 0%,#aaa69e 55%,#3b3028 100%)"></div><div class="meta"><svg width="13" height="13" viewBox="0 0 14 14"><path fill="#7a5a37" d="M1 3h12v10H1z"/></svg>02 MAR 2022<br><svg width="11" height="13" viewBox="0 0 12 14"><path fill="#7a5a37" d="M6 0a5 5 0 015 5c0 4-5 9-5 9S1 9 1 5a5 5 0 015-5z"/></svg>Waikato</div></div>
  <div class="proj" style="left:1083px"><div class="ph" role="img" aria-label="Project photo: white weatherboard cottage" style="background:linear-gradient(180deg,#b9c6d2 0%,#e3e4e2 50%,#5b7d3d 100%)"></div><div class="meta"><svg width="13" height="13" viewBox="0 0 14 14"><path fill="#7a5a37" d="M1 3h12v10H1z"/></svg>02 MAR 2022<br><svg width="11" height="13" viewBox="0 0 12 14"><path fill="#7a5a37" d="M6 0a5 5 0 015 5c0 4-5 9-5 9S1 9 1 5a5 5 0 015-5z"/></svg>Hamilton</div></div>
</section>

<section class="abs contact">
  <h2 class="abs title h2" style="top:58px"><em>Get in</em> Touch</h2>
  <div class="info" style="top:136px"><span class="c"><svg width="30" height="34" viewBox="0 0 30 34" fill="none" stroke="#7a5a37" stroke-width="2.4"><path d="M15 3a9 9 0 019 9c0 7-9 15-9 15S6 19 6 12a9 9 0 019-9z"/><circle cx="15" cy="12" r="3"/><path d="M4 31h22"/></svg></span><div><h5>Address:</h5><p>Rowan Kettleby<br>Hamilton, Waikato.</p></div></div>
  <div class="info" style="top:237px"><span class="c"><svg width="32" height="32" viewBox="0 0 24 24"><path fill="#7a5a37" d="M6.6 10.8a15 15 0 006.6 6.6l2.2-2.2a1 1 0 011-.25 11 11 0 003.6.6 1 1 0 011 1V20a1 1 0 01-1 1A17 17 0 013 4a1 1 0 011-1h3.5a1 1 0 011 1c0 1.3.2 2.5.6 3.6a1 1 0 01-.25 1z"/></svg></span><div><h5>Phone:</h5><p>021 555 0148</p></div></div>
  <div class="info" style="top:342px"><span class="c"><svg width="34" height="26" viewBox="0 0 34 26"><rect width="34" height="26" rx="2" fill="#7a5a37"/><path d="M2 3l15 12L32 3" stroke="#fff" stroke-width="2.4" fill="none"/></svg></span><div><h5>Email:</h5><p>studio@hollowaycoatings.co.nz</p></div></div>

  <div class="field" style="left:511px;top:137px;width:283px;height:49px"><svg width="11" height="12" viewBox="0 0 12 12"><circle cx="6" cy="3.5" r="3" fill="#b2b5bb"/><path d="M0 12a6 5 0 0112 0z" fill="#b2b5bb"/></svg>First Name</div>
  <div class="field" style="left:805px;top:137px;width:283px;height:49px"><svg width="11" height="12" viewBox="0 0 12 12"><circle cx="6" cy="3.5" r="3" fill="#b2b5bb"/><path d="M0 12a6 5 0 0112 0z" fill="#b2b5bb"/></svg>Last Name</div>
  <div class="field" style="left:511px;top:199px;width:283px;height:49px"><svg width="12" height="12" viewBox="0 0 24 24"><path fill="#b2b5bb" d="M6.6 10.8a15 15 0 006.6 6.6l2.2-2.2a1 1 0 011-.25 11 11 0 003.6.6 1 1 0 011 1V20a1 1 0 01-1 1A17 17 0 013 4a1 1 0 011-1h3.5a1 1 0 011 1c0 1.3.2 2.5.6 3.6a1 1 0 01-.25 1z"/></svg>Your Phone</div>
  <div class="field" style="left:805px;top:199px;width:283px;height:49px"><svg width="14" height="11" viewBox="0 0 14 11"><rect width="14" height="11" fill="#b2b5bb"/><path d="M1 1l6 5 6-5" stroke="#fff" fill="none"/></svg>Your Email</div>
  <div class="field msg" style="left:511px;top:264px;width:577px;height:111px"><svg width="13" height="12" viewBox="0 0 13 12"><ellipse cx="6.5" cy="5" rx="6.5" ry="5" fill="#b2b5bb"/></svg>Message</div>
  <div class="btn" style="left:511px;top:392px;width:155px;height:47px;background:var(--brown);color:#fff">Send Message</div>
</section>

<footer class="abs footer">
  <div class="abs flogo">HOLLOWAY<br>COATINGS</div>
  <div class="fcol" style="left:367px"><h6>Quick Links</h6><ul><li><i></i>Home</li><li><i></i>About</li><li><i></i>Services</li><li><i></i>Testimonials</li><li><i></i>Projects</li><li><i></i>Contact</li></ul></div>
  <div class="fcol" style="left:622px"><h6>Other Links</h6><ul><li><i></i>Privacy Policy</li><li><i></i>Terms Of Use</li><li><i></i>Legal Support</li><li><i></i>Site Map</li></ul></div>
  <div class="fcol" style="left:880px"><h6>Contact Info</h6><ul>
    <li><svg width="10" height="13" viewBox="0 0 12 14" style="margin:6px 10px 0 0;flex:none"><path fill="#7a5a37" d="M6 0a5 5 0 015 5c0 4-5 9-5 9S1 9 1 5a5 5 0 015-5z"/></svg>Rowan Kettleby<br>Hamilton, Waikato.</li>
    <li style="margin-top:8px"><svg width="12" height="12" viewBox="0 0 24 24" style="margin:6px 10px 0 0;flex:none"><path fill="#7a5a37" d="M6.6 10.8a15 15 0 006.6 6.6l2.2-2.2a1 1 0 011-.25 11 11 0 003.6.6 1 1 0 011 1V20a1 1 0 01-1 1A17 17 0 013 4a1 1 0 011-1h3.5a1 1 0 011 1c0 1.3.2 2.5.6 3.6a1 1 0 01-.25 1z"/></svg>021 555 0148</li>
    <li style="margin-top:8px"><svg width="13" height="10" viewBox="0 0 14 11" style="margin:7px 10px 0 0;flex:none"><rect width="14" height="11" fill="#7a5a37"/></svg>studio@hollowaycoatings.co.nz</li>
  </ul></div>
  <div class="abs rule" style="top:271px"></div>
  <div class="abs badge" role="img" aria-label="Velnor paint and accredited painter badges">
    <span class="panel" style="width:135px"></span>
    <span class="panel" style="width:340px"></span>
    <span class="tab"></span>
  </div>
  <div class="abs rule" style="top:347px"></div>
</footer>
<div class="abs copy">© 2022 <b>HOLLOWAY COATINGS</b> &nbsp;|&nbsp; All Rights Reserved</div>

</body>
</html>
```